Business Card & Letterhead Design

We a financial advice company based in Australia. We provide advice to wealthy farmers.

We are changing our business name FROM Palomar Financial TO Bluegate Wealth and we need a new letterhead and double sided business card design

Attached is designs from our previous branding (Palomar Financial) as it includes all the details we require on the new Bluegate Wealth business cards and letterhead.

```html
<!DOCTYPE html>
<html lang="en">
<head>
<meta charset="utf-8">
<title>Bluegate Wealth Stationery</title>
<link href="https://fonts.googleapis.com/css2?family=Source+Sans+3:wght@400;600;700&display=swap" rel="stylesheet">
<style>
:root{
  --stage:#000;
  --paper:#fff;
  --ink:#3a3a3a;
  --ink-soft:#555;
  --slate:#4a4b4e;
  --slate-light:#6a6d72;
  --stripe:#cfc9c2;
  --stripe-soft:#e6e2dd;
  --on-dark:#fff;
}
*{margin:0;padding:0;box-sizing:border-box}
html,body{width:1200px;height:999px;overflow:hidden;background:var(--stage)}
body{position:relative;font-family:"Source Sans 3",Arial,sans-serif;color:var(--ink)}
.abs{position:absolute}

/* Letterhead */
.letterhead{left:38px;top:40px;width:708px;height:917px;background:var(--paper);overflow:hidden}
.brand{text-align:center}
.brand .mark{width:44px;height:44px;border:2.5px solid var(--ink);border-radius:50%;margin:0 auto 6px}
.brand .name{font-size:22px;font-weight:400;letter-spacing:1px;color:var(--ink);text-transform:uppercase;line-height:1;white-space:nowrap}
.brand .tag{font-size:7.5px;letter-spacing:3.2px;color:var(--ink-soft);text-transform:uppercase;margin-top:2px;white-space:nowrap}
.lh-brand{left:40px;top:46px;width:228px}
.lh-brand .name{font-size:24px;letter-spacing:1.2px}
.lh-brand .tag{font-size:8px;letter-spacing:3.6px}
.entity{left:526px;top:42px;font-size:11px;font-weight:600;line-height:14px;color:var(--ink)}
.watermark{left:162px;top:300px;width:370px;height:370px;border:22px solid #ebebeb;border-radius:50%}
.salutation{left:59px;top:228px;font-size:13px}
.letter-body{left:44px;top:287px;width:618px;font-size:13.1px;line-height:16.7px;text-align:justify;color:var(--ink)}
.letter-body p{margin-bottom:16.7px}
.letter-body p:first-child{text-indent:41px}
.lh-wave{left:0;top:728px}
.lh-foot{font-size:11px;line-height:14.2px;color:var(--on-dark)}
.foot-licence{left:27px;top:779px}
.foot-address{left:302px;top:815px}
.foot-contact{left:497px;top:801px}
.foot-contact li{list-style:none;display:flex;align-items:center;gap:12px;height:15px}
.foot-contact li.gap{margin-top:4px}
.foot-contact svg{width:11px;height:11px;fill:var(--on-dark)}
.lh-motto{left:0;top:885px;width:708px;text-align:center;font-size:12.5px;font-weight:700;letter-spacing:1px;color:var(--slate)}
.lh-base{left:0;top:904px;width:708px;height:13px;background:var(--slate)}

/* Business card front */
.card{width:346px;height:197px;overflow:hidden}
.card-front{left:806px;top:183px;background:var(--paper)}
.cf-brand{left:10px;top:18px;width:150px}
.cf-brand .mark{width:30px;height:30px;border-width:2px;margin-bottom:4px}
.cf-brand .name{font-size:14.5px}
.cf-brand .tag{font-size:5px;letter-spacing:2px}
.holder{left:224px;top:33px;font-size:7px;font-weight:600;line-height:10px;color:var(--ink)}
.holder .person{font-size:12.5px;font-weight:700;line-height:14px;margin-bottom:3px}
.holder .person small{font-size:4.5px;font-weight:400}
.cf-wave{left:0;top:86px}
.cf-text{color:var(--on-dark);font-size:7.5px;line-height:10.2px}
.cf-quote{left:14px;top:124px;font-size:8.5px}
.cf-contact{left:19px;top:136px}
.cf-contact li{list-style:none;display:flex;align-items:center;gap:4px}
.cf-contact svg{width:6px;height:6px;fill:var(--on-dark)}
.cf-address{left:218px;top:133px}
.cf-motto{left:218px;top:177px;font-size:8px;font-weight:600;font-style:italic;letter-spacing:1px}

/* Business card back */
.card-back{left:806px;top:415px;background:radial-gradient(ellipse at 55% 35%,var(--slate-light) 0%,var(--slate) 70%)}
.cb-mark{left:142px;top:20px;width:61px;height:61px;border:2.5px solid var(--on-dark);border-radius:50%}
.services{left:0;top:89px;width:346px;text-align:center;color:var(--on-dark);font-size:10.5px;letter-spacing:1.3px;line-height:14px}
.licensee{left:0;top:156px;width:346px;text-align:center;color:var(--on-dark);font-size:7px;font-weight:600;line-height:10px}
</style>
</head>
<body>

<section class="letterhead abs">
  <div class="watermark abs" aria-hidden="true"></div>
  <div class="brand lh-brand abs">
    <div class="mark"></div>
    <div class="name">Bluegate Wealth</div>
    <div class="tag">Strategic Financial Advice</div>
  </div>
  <div class="entity abs">
    Kestrel Holdings Pty Ltd<br>
    ATF The Marlow Investment<br>
    Trust T/AS Palomar Financial<br>
    ABN: 51 203 889 416<br>
    Corporate Authorised<br>
    Representative of Meridian<br>
    Advice Partners Limited
  </div>

  <p class="salutation abs">Dear Sir</p>
  <div class="letter-body abs">
    <p>Lorem ipsum dolor sit amet, consectetur adipiscing elit. Integer eu odio mattis, pulvinar turpis quis, faucibus nisl. Proin feugiat, erat vitae cursus pharetra, enim est semper ligula, in malesuada orci nisl et diam. Etiam elementum metus ac fringilla vulputate. Etiam mattis ligula sed ante mollis bibendum. Orci varius natoque penatibus et magnis dis parturient montes, nascetur ridiculus mus.</p>
    <p>Ut nibh augue, blandit ac orci ac, rutrum congue enim. Suspendisse gravida vulputate felis, quis interdum orci tincidunt quis. Praesent imperdiet maximus neque. Mauris ut dui enim. Nullam at efficitur elit. Donec ante ipsum, fermentum at lectus vel, blandit vulputate ante. Proin luctus suscipit diam id vestibulum. Morbi malesuada id mauris eget ullamcorper.</p>
    <p>Donec varius orci purus, vitae aliquam libero volutpat id. Integer sed imperdiet libero. Aliquam accumsan, risus sit amet ornare consectetur, turpis felis dictum justo, non rhoncus mauris dui sed velit. Pellentesque habitant morbi tristique senectus et netus et malesuada fames ac turpis egestas. Pellentesque tincidunt vitae ligula nec imperdiet. Donec sed congue enim. Nullam elementum faucibus nulla nec vestibulum. Sed at tempor ligula. In quis vulputate nunc. Integer at gravida lacus, ac tristique risus. Sed at vulputate nulla.</p>
    <p>Praesent blandit nunc eu efficitur commodo. In tempor nisi ex, vel venenatis ante vestibulum a. Duis vestibulum nibh a erat sagittis, nec euismod lorem varius. Nam ultricies turpis sed justo sollicitudin volutpat. Morbi sed mollis eros. Sed quis tortor id enim vehicula porttitor. Curabitur non aliquam ex. Phasellus dignissim fermentum elit, at finibus ligula mattis eget.</p>
  </div>

  <svg class="lh-wave abs" width="708" height="158" viewBox="0 0 708 158" aria-hidden="true">
    <defs>
      <radialGradient id="lhSlate" cx="55%" cy="60%" r="70%">
        <stop offset="0" stop-color="#66696e"/><stop offset="1" stop-color="#47484b"/>
      </radialGradient>
    </defs>
    <path d="M0 22 C120 -4 240 2 360 30 C480 58 600 34 708 4 L708 157 L0 157 Z" fill="var(--stripe-soft)"/>
    <path d="M0 30 C120 6 240 12 360 40 C480 66 600 44 708 14 L708 157 L0 157 Z" fill="var(--stripe)"/>
    <path d="M0 38 C120 16 240 22 360 50 C480 76 600 54 708 24 L708 157 L0 157 Z" fill="#fff"/>
    <path d="M0 46 C120 26 240 32 360 60 C480 86 600 64 708 34 L708 157 L0 157 Z" fill="url(#lhSlate)"/>
  </svg>
  <div class="lh-foot foot-licence abs">
    Meridian Advice Partners Limited<br>
    ABN 62 117 430 585<br>
    Australian Financial Services Licence<br>
    Licence Number 318 902<br>
    Principle Address: 210 Wattle St<br>
    PO Box 4410 Ashford VIC 3150
  </div>
  <div class="lh-foot foot-address abs">
    Suite 4A, 18 Harlow St<br>
    Riverton Heights QLD 4210<br>
    PO Box 1120<br>
    Westbrook QLD 4212
  </div>
  <ul class="lh-foot foot-contact abs">
    <li><svg viewBox="0 0 12 12"><path d="M3 1 L5 3.5 L4 5 C5 7 6 8 7.5 8.5 L9 7.5 L11 9.5 L9.5 11 C5 10.5 1.5 7 1 2.5 Z"/></svg>(07) 3000 1234</li>
    <li><svg viewBox="0 0 12 12"><rect x="3" y="1" width="6" height="3"/><rect x="1" y="5" width="10" height="4"/><rect x="3" y="8" width="6" height="3"/></svg>(07) 3000 5678</li>
    <li class="gap"><svg viewBox="0 0 12 12"><path d="M1 3 L11 3 L11 10 L1 10 Z M1 3 L6 7 L11 3" stroke="#47484b" stroke-width="0.8"/></svg>admin@palomarfinancial.com.au</li>
    <li><svg viewBox="0 0 12 12"><circle cx="6" cy="6" r="5"/><path d="M1 6 H11 M6 1 V11" stroke="#47484b" stroke-width="0.8"/></svg>www.palomarfinancial.com.au</li>
  </ul>
  <p class="lh-motto abs">A referral built business</p>
  <div class="lh-base abs"></div>
</section>

<section class="card card-front abs">
  <div class="brand cf-brand abs">
    <div class="mark"></div>
    <div class="name">Bluegate Wealth</div>
    <div class="tag">Strategic Financial Advice</div>
  </div>
  <div class="holder abs">
    <div class="person">Sam Carter <small>BBus DipFP CFP</small></div>
    Managing Director<br>
    Authorised Representative
  </div>
  <svg class="cf-wave abs" width="346" height="111" viewBox="0 0 346 111" aria-hidden="true">
    <defs>
      <radialGradient id="cfSlate" cx="45%" cy="55%" r="65%">
        <stop offset="0" stop-color="#6a6d72"/><stop offset="1" stop-color="#47484b"/>
      </radialGradient>
    </defs>
    <path d="M0 20 C70 6 130 8 190 22 C250 36 300 26 346 4 L346 111 L0 111 Z" fill="var(--stripe-soft)"/>
    <path d="M0 25 C70 11 130 13 190 27 C250 41 300 31 346 9 L346 111 L0 111 Z" fill="var(--stripe)"/>
    <path d="M0 29 C70 15 130 17 190 31 C250 45 300 35 346 13 L346 111 L0 111 Z" fill="#fff"/>
    <path d="M0 33 C70 20 130 22 190 36 C250 50 300 40 346 18 L346 111 L0 111 Z" fill="url(#cfSlate)"/>
  </svg>
  <p class="cf-text cf-quote abs">‘Financial peace of mind’</p>
  <ul class="cf-text cf-contact abs">
    <li><svg viewBox="0 0 12 12"><circle cx="6" cy="6" r="6"/></svg>(07) 3000 1234</li>
    <li><svg viewBox="0 0 12 12"><rect x="1" y="2" width="10" height="8"/></svg>(07) 3000 5678</li>
    <li><svg viewBox="0 0 12 12"><rect x="3" y="0" width="6" height="12" rx="1"/></svg>0400 000 123</li>
    <li><svg viewBox="0 0 12 12"><path d="M0 2 H12 V10 H0 Z"/></svg>sam@palomarfinancial.com.au</li>
    <li><svg viewBox="0 0 12 12"><circle cx="6" cy="6" r="6"/></svg>www.palomarfinancial.com.au</li>
  </ul>
  <div class="cf-text cf-address abs">
    Suite 4A, 18 Harlow St<br>
    Riverton Heights QLD 4210<br>
    PO Box 1120<br>
    Westbrook QLD 4212
  </div>
  <p class="cf-text cf-motto abs">A referral built business</p>
</section>

<section class="card card-back abs">
  <div class="cb-mark abs" aria-hidden="true"></div>
  <div class="services abs">
    Life &amp; TPD Insurance<br>
    Income Protection<br>
    Financial Planning<br>
    Retirement Planning
  </div>
  <div class="licensee abs">
    Meridian Advice Partners Limited<br>
    Australian Financial Services Licensee License Number 318902
  </div>
</section>

</body>
</html>
```